Web Design for a recruitment company

Website is for a recruitment company, with a particular focus on temporary staff, trades, skilled, and unskilled labour markets. Website will consist of a home page design and separate design for additional pages. Website will be implemented as a template in SharePoint. There is a separate design project for a new logo and look colours will need to be co-ordinated.

Target Market(s)

Company executives in the construction and trades areas looking for staff. Trades people, skilled and unskilled labourers looking for work.

Industry/Entity Type

It Company

Number of Pages Required

2 page

Requirements
Must have
• Looking for Home Page design plus design for additional pages.
• .
Nice to have
• Good Crew | Good Site is the firms byline, company name is TOV Staffing. They will be in the Logo (separate project) but may also appear elsewhere in the design.
• Company values (attached file) may be reflected in the design where practical.

```html
<!DOCTYPE html>
<html lang="en">
<head>
<meta charset="utf-8">
<title>TOV Staffing — Home</title>
<link href="https://fonts.googleapis.com/css2?family=Lato:wght@400;700&family=Oswald:wght@400&family=Arvo:wght@700&display=swap" rel="stylesheet">
<style>
:root{
  --ink:#2b2b2b;
  --text:#555;
  --muted:#777;
  --line:#d9d9d9;
  --page:#ffffff;
  --band:#ececec;
  --nav-top:#f6f6f6;
  --nav-bot:#dedede;
  --blue:#1565b7;
  --grey-circle:#6a6a6a;
  --btn:#5e5e5e;
  --panel:#8a8a8a;
  --panel-dark:#777;
  --footer:#1d1d1d;
  --footer-low:#262626;
  --footer-text:#a9a9a9;
  --date:#444;
}
*{margin:0;padding:0;box-sizing:border-box}
html,body{width:714px;height:1200px;overflow:hidden}
body{position:relative;background:var(--page);font-family:"Lato",Arial,sans-serif;color:var(--text)}
.abs{position:absolute}

/* header */
.site-header{left:0;top:0;width:714px;height:49px;background:var(--page)}
.brand{left:80px;top:10px;display:flex;align-items:center;gap:8px}
.brand-mark{width:28px;height:28px;border-radius:50%;background:#3a3a3a}
.brand-name{font-weight:700;font-size:19px;color:var(--ink);line-height:1}
.brand-byline{font-size:9.5px;color:var(--ink);margin-top:3px}
.tollfree{right:78px;top:17px;display:flex;align-items:center;gap:6px;font-size:10.5px;color:#333}
.tollfree .dot{width:17px;height:17px;border-radius:50%;background:#111;display:flex;align-items:center;justify-content:center}

.main-nav{left:0;top:49px;width:714px;height:28px;background:linear-gradient(var(--nav-top),var(--nav-bot))}
.main-nav ul{list-style:none;display:flex;position:absolute;left:80px;top:9px;font-size:9px;color:#333}
.main-nav li{padding:0 16px;border-left:1px solid #c4c4c4}
.main-nav li:first-child{padding-left:0;border-left:0}
.search{left:513px;top:55px;width:123px;height:16px;background:#fff;border:1px solid #e0e0e0;font-size:6.5px;color:#999;padding:4px 4px;font-style:italic}
.search svg{position:absolute;right:3px;top:2px}

/* hero */
.hero{left:0;top:77px;width:714px;height:281px;background:linear-gradient(100deg,#d9d9d9 0%,#8b8b8b 30%,#3d3d3d 60%,#6a6a6a 85%,#bdbdbd 100%)}
.hero h1{position:absolute;left:0;width:714px;top:192px;text-align:center;font-family:"Oswald",Arial,sans-serif;font-weight:400;font-size:21px;color:#fff;text-shadow:0 1px 3px rgba(0,0,0,.6);letter-spacing:-.3px}

/* services */
.services{left:0;top:358px;width:714px;height:238px;background:var(--band)}
.service{position:absolute;top:28px;width:180px;text-align:center}
.service .icon{width:72px;height:72px;border-radius:50%;margin:0 auto;display:flex;align-items:center;justify-content:center;background:radial-gradient(circle at 50% 35%,#8a8a8a,#4e4e4e)}
.service .icon.candidate{background:radial-gradient(circle at 50% 35%,#2a7fd4,#0e4f98)}
.service h2{font-weight:400;font-size:14px;color:var(--ink);margin-top:19px}
.service p{font-size:7.3px;line-height:11px;color:#444;margin-top:8px}
.btn{display:inline-block;background:var(--btn);color:#fff;font-size:7.5px;font-weight:700;padding:4px 9px;border-radius:1px;margin-top:13px}
.divider-v{position:absolute;top:45px;width:1px;height:175px;background:#dcdcdc}

/* welcome */
.welcome{left:78px;top:610px;width:332px}
.welcome h2{font-weight:400;font-size:13px;color:var(--ink);padding-bottom:4px;border-bottom:3px solid #eee}
.welcome h2 b{font-family:"Arvo",Georgia,serif;font-size:18px;margin-left:3px}
.video{left:78px;top:647px;width:134px;height:83px;background:linear-gradient(135deg,#7b8794,#4f5d6a 55%,#2a3037)}
.video .bar{position:absolute;left:0;bottom:0;width:134px;height:10px;background:#111}
.video .bar i{position:absolute;left:14px;top:4px;width:60px;height:2px;background:#c22}
.video .play{position:absolute;left:55px;top:30px;width:24px;height:17px;border-radius:3px;background:#d2d2d2;display:flex;align-items:center;justify-content:center}
.copy{font-size:7.3px;line-height:12.4px;color:#666}
.copy-side{left:225px;top:645px;width:185px}
.copy-full{left:78px;top:737px;width:334px}
.readmore{left:79px;top:771px;font-size:8px;color:#333}

/* appointment */
.appointment{left:437px;top:582px;width:200px;height:200px;background:var(--panel);box-shadow:0 1px 2px rgba(0,0,0,.2)}
.appointment h3{height:41px;background:var(--panel-dark);color:#fff;font-weight:400;font-size:13.5px;text-align:center;padding-top:13px;border-bottom:1px solid #6a6a6a}
.field{position:absolute;background:#fff;font-size:6.5px;color:#777;padding:6px 5px;border-radius:1px}
.submit{position:absolute;left:76px;top:175px;width:56px;height:17px;border-radius:9px;background:#222;color:#fff;font-size:9px;font-weight:700;text-align:center;line-height:17px;border:1px solid #666}
.fold{position:absolute;top:0;width:0;height:0;border-bottom:12px solid #777}

.soft-rule{left:120px;top:810px;width:474px;height:1px;background:linear-gradient(90deg,transparent,#ddd,transparent)}

/* info boxes */
.box{position:absolute;top:838px;width:179px;height:145px;border:1px solid #ddd;background:#fff;box-shadow:0 4px 4px -3px rgba(0,0,0,.2)}
.box h3{font-weight:400;font-size:12px;color:var(--ink);margin:7px 7px 0;padding-bottom:5px;border-bottom:1px solid #eee}
.team-photo{position:absolute;left:6px;top:31px;width:166px;height:62px;background:linear-gradient(#c9ced3,#8d939a 60%,#3f444a);border:1px solid #ccc}
.box .small{font-size:6.8px;line-height:10.5px;color:#666}
.viewall{position:absolute;right:9px;bottom:6px;font-size:7.5px;color:#333}
.job{position:absolute;left:6px;width:166px;height:48px}
.job .thumb{position:absolute;left:0;top:2px;width:35px;height:35px;border:1px solid #ddd;display:flex;align-items:center;justify-content:center}
.job .thumb span{width:17px;height:17px;border-radius:50%;background:#3a3a3a}
.job .t{position:absolute;left:42px;top:0;font-size:8.3px;color:#333}
.job .d{position:absolute;left:42px;top:11px;width:124px}
.news{position:absolute;left:6px;width:166px}
.news .date{position:absolute;left:0;top:2px;width:22px;height:24px;background:var(--date);color:#fff;text-align:center;font-size:5.8px;font-weight:700;line-height:8px;padding-top:1px}
.news .date b{display:block;font-size:10px;line-height:12px;background:#666}
.news .t{position:absolute;left:30px;top:0;font-size:6.8px;font-weight:700;color:#333}
.news .d{position:absolute;left:30px;top:10px;width:136px}

/* footer */
.footer{left:0;top:1011px;width:714px;height:109px;background:var(--footer);color:var(--footer-text)}
.footer h4{position:absolute;font-weight:400;font-size:10px;color:#e6e6e6;letter-spacing:.2px}
.footer .small{font-size:7.3px;line-height:14px}
.footer .sep{position:absolute;top:17px;width:1px;height:78px;background:#3a3a3a}
.newsletter{position:absolute;left:273px;top:48px;width:169px;height:24px;border:1px solid #3d3d3d;font-size:7.3px;padding:7px 9px}
.newsletter span{position:absolute;right:9px;top:6px}
.reach{position:absolute;right:79px;top:38px;text-align:right}
.reach b{color:#ddd;font-weight:700}
.footer-low{left:0;top:1120px;width:714px;height:80px;background:var(--footer-low);border-top:1px solid #333;color:#9a9a9a}
.footer-nav{position:absolute;left:0;width:714px;top:12px;text-align:center;font-size:7.5px;letter-spacing:.2px}
.footer-nav i{font-style:normal;margin:0 9px;color:#666}
.socials{position:absolute;left:319px;top:34px;display:flex;gap:6px}
.socials span{width:14px;height:14px;border-radius:50%;background:#5a5a5a}
.socials span:first-child{background:#f2f2f2}
.legal{position:absolute;left:0;width:714px;top:60px;text-align:center;font-size:7.3px;color:#8a8a8a}
</style>
</head>
<body>

<header class="abs site-header">
  <div class="abs brand">
    <div class="brand-mark"></div>
    <div>
      <div class="brand-name">TOV Staffing</div>
      <div class="brand-byline">Good Crew | Good Site</div>
    </div>
  </div>
  <div class="abs tollfree">
    <span class="dot"><svg width="9" height="9" viewBox="0 0 24 24"><path fill="#fff" d="M6.6 10.8a15 15 0 0 0 6.6 6.6l2.2-2.2c.3-.3.7-.4 1-.2 1.1.4 2.3.6 3.6.6.6 0 1 .4 1 1V20c0 .6-.4 1-1 1A17 17 0 0 1 3 4c0-.6.4-1 1-1h3.5c.6 0 1 .4 1 1 0 1.3.2 2.5.6 3.6.1.3 0 .7-.2 1z"/></svg></span>
    Toll Free 800 555 0142
  </div>
</header>

<nav class="abs main-nav">
  <ul>
    <li>Home</li><li>About Us</li><li>For Jobseekers</li><li>For Employers</li><li>Contact Us</li>
  </ul>
</nav>
<div class="abs search">Search...
  <svg width="11" height="11" viewBox="0 0 12 12"><circle cx="5" cy="5" r="3.5" fill="none" stroke="#333" stroke-width="1.3"/><path d="M7.6 7.6 11 11" stroke="#333" stroke-width="1.5"/></svg>
</div>

<section class="abs hero" role="img" aria-label="Photo of a row of business people in suits seated in a waiting room">
  <h1>We're Good at putting people in their Place</h1>
</section>

<section class="abs services">
  <div class="service" style="left:73px">
    <div class="icon candidate">
      <svg width="40" height="40" viewBox="0 0 40 40"><circle cx="23" cy="16" r="10" fill="none" stroke="#fff" stroke-width="3"/><circle cx="23" cy="13" r="3.5" fill="#fff"/><path d="M17 22c1-4 11-4 12 0" fill="#fff"/><path d="M16 23 6 33" stroke="#fff" stroke-width="4" stroke-linecap="round"/></svg>
    </div>
    <h2>Candidate</h2>
    <p>Lorem ipsum dolor sit amet, consectet adipiscing elit, sed diam nonummy euismod tincidunt ut laoreet dolore aliquam erat volutpat.</p>
    <span class="btn">Read More</span>
  </div>
  <div class="divider-v" style="left:260px"></div>
  <div class="service" style="left:267px">
    <div class="icon">
      <svg width="40" height="40" viewBox="0 0 40 40"><circle cx="20" cy="20" r="14" fill="none" stroke="#fff" stroke-width="4" stroke-dasharray="18 4"/><circle cx="17" cy="17" r="3.5" fill="#fff"/><circle cx="23" cy="16" r="3" fill="#fff"/><path d="M11 27c1-5 11-5 12 0zM19 24c1-4 9-4 10 0z" fill="#fff"/></svg>
    </div>
    <h2>Clients</h2>
    <p>Lorem ipsum dolor sit amet, consectet adipiscing elit, sed diam nonummy euismod tincidunt ut laoreet dolore aliquam erat volutpat.</p>
    <span class="btn">Read More</span>
  </div>
  <div class="divider-v" style="left:453px"></div>
  <div class="service" style="left:462px">
    <div class="icon">
      <svg width="36" height="36" viewBox="0 0 36 36"><rect x="6" y="11" width="24" height="17" rx="2" fill="#fff"/><rect x="13" y="7" width="10" height="5" rx="1" fill="none" stroke="#fff" stroke-width="2"/><rect x="6" y="17" width="24" height="1.5" fill="#777"/></svg>
    </div>
    <h2>Consultants</h2>
    <p>Lorem ipsum dolor sit amet, consectet adipiscing elit, sed diam nonummy euismod tincidunt ut laoreet dolore aliquam erat volutpat.</p>
    <span class="btn">Read More</span>
  </div>
</section>

<section class="abs welcome"><h2>Welcome to <b>TOV Staffing</b></h2></section>
<div class="abs video" role="img" aria-label="Video still of a hand placing a jigsaw puzzle piece">
  <div class="play"><svg width="8" height="8" viewBox="0 0 8 8"><path d="M1 0 8 4 1 8z" fill="#333"/></svg></div>
  <div class="bar"><i></i></div>
</div>
<p class="abs copy copy-side">Lorem ipsum dolor sit amet, consectetue adipli scing elit, sed diam nonummy nibh euismodmlp tincidunt ut laoreet dolore magna aliquam eratl volutpat. Ut wisi enim ad minim veniam, quisop nostrud exerci tation ullamcorper suscipi lobortis nisl ut aliquip ex ea commodo consequa am vopetept</p>
<p class="abs copy copy-full">Lorem ipsum dolor sit amet, consectetuer adipli scing elit, sed diam nonummy nibh euismodmlp tincidunt ut laoreet dolore magna aliquam eratl volutpat.</p>
<span class="abs readmore">Read More [+]</span>

<aside class="abs appointment">
  <span class="fold" style="left:-10px;border-left:10px solid transparent"></span>
  <span class="fold" style="right:-10px;border-right:10px solid transparent"></span>
  <h3>Request an Appointment</h3>
  <div class="field" style="left:11px;top:51px;width:178px;height:19px">Name *</div>
  <div class="field" style="left:11px;top:75px;width:178px;height:19px">Email *</div>
  <div class="field" style="left:11px;top:99px;width:86px;height:19px">Company *</div>
  <div class="field" style="left:103px;top:99px;width:86px;height:19px">Phone *</div>
  <div class="field" style="left:11px;top:123px;width:178px;height:42px">Message</div>
  <div class="submit">SUBMIT</div>
</aside>

<div class="abs soft-rule"></div>

<section class="box" style="left:78px">
  <h3>Meet Our Team</h3>
  <div class="team-photo" role="img" aria-label="Group photo of the recruitment team"></div>
  <p class="small abs" style="left:7px;top:98px;width:166px">Lorem ipsum dolor sit amet, consecte adipiscing elit, sed diam nonummy nibh euismod tincidunt tinciduntut</p>
  <span class="viewall">View All [+]</span>
</section>

<section class="box" style="left:268px">
  <h3>Featured Jobs</h3>
  <div class="job" style="top:30px">
    <div class="thumb"><span></span></div>
    <div class="t">Euismod Tincidunt Ut Laoreet</div>
    <div class="d small">Lorem ipsum dolor si ametconetuge sed diay nibhdl tincidunt ut l dolore mag diay nibhdl</div>
  </div>
  <div class="abs" style="left:6px;top:76px;width:166px;height:1px;background:#eee"></div>
  <div class="job" style="top:80px">
    <div class="thumb"><span></span></div>
    <div class="t">Euismod Tincidunt Ut Laoreet</div>
    <div class="d small">Lorem ipsum dolor si ametconetuge sed diay nibhdl tincidunt ut l dolore mag diay nibhdl</div>
  </div>
  <span class="viewall">View All [+]</span>
</section>

<section class="box" style="left:458px">
  <h3>Latest News</h3>
  <div class="news" style="top:31px">
    <div class="date">NOV<b>06</b></div>
    <div class="t">Lorem ipsum This is dolor sit amet</div>
    <div class="d small">Lorem ipsum dolor si ametconetug sed diay nibhdl tincidunt ut l dolore m diay nibhdl</div>
  </div>
  <div class="news" style="top:85px">
    <div class="date">NOV<b>06</b></div>
    <div class="t">Lorem ipsum This is dolor sit amet</div>
    <div class="d small">Lorem ipsum dolor si ametconetug sed diay nibhdl tincidunt ut l dolore m diay nibhdl</div>
  </div>
  <span class="viewall">View All [+]</span>
</section>

<footer class="abs footer">
  <h4 style="left:80px;top:24px">TOV STAFFING</h4>
  <p class="small abs" style="left:79px;top:40px;width:160px">000 Vestibulum suscipit tellus fermentum nibh blandit congue In ipsum pretium suscipit ut quam.<br>000 000</p>
  <div class="sep" style="left:250px"></div>
  <h4 style="left:293px;top:24px">SIGN UP FOR NEWSLETTER</h4>
  <div class="newsletter">Enter your email here <span>&#8594;</span></div>
  <div class="sep" style="left:464px"></div>
  <h4 style="right:79px;top:24px">REACH US</h4>
  <p class="small reach"><b>M:</b> (555) 010 2240<br>(555) 010 2240<br><b>O:</b> (555) 010 2240<br><b>E:</b> info@tovstaffing.com</p>
</footer>

<div class="abs footer-low">
  <div class="footer-nav">HOME<i>|</i>ABOUT<i>|</i>FOR JOBSEEKERS<i>|</i>FOR EMPLOYERS<i>|</i>CONTACT</div>
  <div class="socials"><span></span><span></span><span></span><span></span></div>
  <div class="legal">Copyright © 2014 TOV Staffing. All Right Reserved.</div>
</div>

</body>
</html>
```